BRL business card

For a business card with our logo

Contact Information for Business Card

Mathéo VRANEL
Founder & CEO
email : ceo@brightlanterncollective.com / www.brightlanterncollective.com /
instagram / facebook / WhatsApp
N°: +590 690 482 517

Colors

Designer to choose colors to be used in the design.

```html
<!DOCTYPE html>
<html lang="en">
<head>
<meta charset="utf-8">
<title>BRL business card</title>
<link rel="stylesheet" href="https://fonts.googleapis.com/css2?family=Cinzel:wght@700&family=Montserrat:wght@400;500&display=swap">
<style>
  :root {
    --stage: #2a2a2a;
    --brand-blue: #1557a8;
    --text-blue: #1f5fbf;
    --brand-orange: #f47420;
    --card-black: #080808;
    --white: #ffffff;
  }
  html, body {
    margin: 0;
    width: 1200px;
    height: 900px;
    overflow: hidden;
    background: var(--stage);
  }
  .canvas {
    position: relative;
    width: 1200px;
    height: 900px;
  }
  .card {
    position: absolute;
    left: 250px;
    width: 700px;
    height: 400px;
    overflow: hidden;
    box-shadow: 0 12px 30px rgba(0,0,0,.5);
  }
  .card--front { top: 35px; background: var(--brand-blue); }
  .card--back { top: 465px; background: var(--card-black); }

  .tile {
    position: absolute;
    background: rgba(255,255,255,.1);
  }

  .brand {
    position: absolute;
    display: flex;
    flex-direction: column;
    align-items: center;
    font-family: "Cinzel", Georgia, serif;
    font-weight: 700;
    letter-spacing: .02em;
    line-height: 1.1;
    text-align: center;
  }
  .brand__dot {
    border-radius: 50%;
    background: var(--brand-orange);
    margin-bottom: 14px;
  }
  .card--front .brand {
    left: 0; right: 0; top: 95px;
    color: var(--white);
    font-size: 36px;
  }
  .card--front .brand__dot { width: 96px; height: 96px; }
  .card--back .brand {
    left: 40px; top: 40px;
    color: var(--text-blue);
    font-size: 24px;
  }
  .card--back .brand__dot { width: 76px; height: 76px; margin-bottom: 10px; }

  .rule {
    position: absolute;
    left: 75px; top: 222px;
    width: 575px; height: 2px;
    background: var(--brand-orange);
  }
  .name-tab {
    position: absolute;
    left: 22px; top: 242px;
    width: 8px; height: 36px;
    background: var(--brand-orange);
  }
  .person {
    position: absolute;
    left: 62px; top: 236px;
  }
  .person__name {
    margin: 0;
    font-family: "Cinzel", Georgia, serif;
    font-weight: 700;
    font-size: 25px;
    color: var(--text-blue);
  }
  .person__role {
    margin: 2px 0 0;
    font-family: "Montserrat", Arial, sans-serif;
    font-size: 18px;
    color: var(--brand-orange);
  }

  .contact {
    position: absolute;
    right: 28px; top: 236px;
    margin: 0; padding: 0;
    list-style: none;
    font-family: "Montserrat", Arial, sans-serif;
    font-size: 17px;
    color: var(--text-blue);
  }
  .contact__item {
    display: flex;
    justify-content: flex-end;
    align-items: center;
    gap: 10px;
    height: 28px;
  }
  .contact__icon {
    width: 22px;
    display: flex;
    justify-content: center;
    color: var(--brand-orange);
    font-weight: 500;
  }
  .social {
    position: absolute;
    right: 28px; top: 330px;
    display: flex;
    gap: 18px;
  }
  .social__badge {
    width: 28px; height: 28px;
    border-radius: 50%;
    background: var(--brand-orange);
  }
  .bands {
    position: absolute;
    left: 0; bottom: 0;
    width: 700px; height: 90px;
  }
</style>
</head>
<body>
<main class="canvas">
  <section class="card card--front" aria-label="Card front">
    <div class="tile" style="left:250px;top:30px;width:36px;height:24px"></div>
    <div class="tile" style="left:330px;top:30px;width:36px;height:24px"></div>
    <div class="tile" style="left:410px;top:50px;width:50px;height:38px"></div>
    <div class="tile" style="left:260px;top:95px;width:50px;height:40px"></div>
    <div class="tile" style="left:480px;top:100px;width:46px;height:38px"></div>
    <div class="brand">
      <span class="brand__dot"></span>
      <span>Bright Lantern</span>
      <span>Collective</span>
    </div>
  </section>

  <section class="card card--back" aria-label="Card back">
    <div class="brand">
      <span class="brand__dot"></span>
      <span>Bright Lantern</span>
      <span>Collective</span>
    </div>

    <div class="rule"></div>
    <div class="name-tab"></div>
    <div class="person">
      <p class="person__name">Mathéo VRANEL</p>
      <p class="person__role">Founder &amp; CEO</p>
    </div>

    <ul class="contact">
      <li class="contact__item">+590 690 482 517 <span class="contact__icon">N°</span></li>
      <li class="contact__item">ceo@brightlanterncollective.com
        <span class="contact__icon">
          <svg width="18" height="14" viewBox="0 0 18 14" fill="none" stroke="currentColor" stroke-width="2"><rect x="1" y="1" width="16" height="12" rx="2"/><path d="M1 2l8 6 8-6"/></svg>
        </span>
      </li>
      <li class="contact__item">www.brightlanterncollective.com
        <span class="contact__icon">
          <svg width="18" height="18" viewBox="0 0 18 18" fill="none" stroke="currentColor" stroke-width="1.5"><circle cx="9" cy="9" r="8"/><ellipse cx="9" cy="9" rx="3.5" ry="8"/><path d="M1 9h16M2.5 5h13M2.5 13h13"/></svg>
        </span>
      </li>
    </ul>

    <div class="social" aria-label="Social profiles">
      <span class="social__badge"></span>
      <span class="social__badge"></span>
      <span class="social__badge"></span>
    </div>

    <svg class="bands" viewBox="0 0 700 90" aria-hidden="true">
      <polygon points="0,18 340,18 370,76 350,76 330,36 0,36" fill="var(--brand-orange)"/>
      <polygon points="0,46 320,46 338,80 0,80" fill="var(--brand-orange)" opacity="0"/>
      <polygon points="0,44 322,44 338,76 0,76" fill="none"/>
      <rect x="0" y="44" width="320" height="12" fill="var(--brand-orange)"/>
      <rect x="378" y="76" width="322" height="14" fill="var(--brand-blue)"/>
    </svg>
  </section>
</main>
</body>
</html>
```